Brochure Design Project

PLEASE USE THE ATTACHED WORD DOC ONLY AS A GUIDE- I WANT TO SEE A TRUE DESIGN AND NOT JUST A RECREATE OF MY CONTENT.

We need a brochure that is geared towards a service mentality. less tech/bold and something very approachable.

we will look for a design concept and then finalize the content laters.

Target Market(s)

nurses and business owners

Industry/Entity Type

Tech

```html
<!DOCTYPE html>
<html lang="en">
<head>
<meta charset="utf-8">
<title>Harborview Pharmacy Services – Trifold Brochure</title>
<link rel="stylesheet" href="https://fonts.googleapis.com/css2?family=Crimson+Text:wght@400;600;700&family=Vollkorn:wght@600;700&display=swap">
<style>
  :root {
    --backdrop: #e4e5e7;
    --paper: #ffffff;
    --panel-tint: #eef5fa;
    --brand-blue: #2b79b5;
    --deep-blue: #1b67a8;
    --soft-blue: #cfe3f1;
    --pale-line: #b9c9d6;
    --ink: #1e1e1e;
    --fold: #dfe6ec;
  }
  * { box-sizing: border-box; margin: 0; padding: 0; }
  html, body { width: 1200px; height: 900px; overflow: hidden; }
  body {
    background: var(--backdrop);
    font-family: "Crimson Text", Georgia, serif;
    color: var(--ink);
    position: relative;
  }
  .brochure {
    position: absolute;
    left: 90px; top: 60px;
    width: 1020px; height: 770px;
    background: var(--paper);
    box-shadow: 0 6px 18px rgba(0,0,0,0.18);
    overflow: hidden;
  }
  .decor { position: absolute; inset: 0; width: 1020px; height: 770px; }
  .panel {
    position: absolute; top: 0;
    width: 340px; height: 770px;
  }
  .panel--intro { left: 0; }
  .panel--services { left: 340px; background: var(--panel-tint); border-left: 1px solid var(--fold); border-right: 1px solid var(--fold); }
  .panel--support { left: 680px; }

  .intro-heading {
    position: absolute; left: 32px; top: 50px; width: 300px;
    font-family: "Vollkorn", Georgia, serif;
    font-weight: 700; font-size: 27px; line-height: 1.15;
    color: var(--brand-blue);
  }
  .feature-list {
    position: absolute; left: 26px; top: 488px; width: 300px;
    list-style: none;
    font-size: 15.5px; line-height: 1.75;
  }
  .feature-list li { position: relative; padding-left: 12px; }
  .feature-list li::before {
    content: ""; position: absolute; left: 0; top: 11px;
    width: 5px; height: 5px; border-radius: 50%;
    background: var(--brand-blue);
  }

  .service-block { margin-bottom: 19px; }
  .panel--services .content { position: absolute; left: 26px; top: 80px; width: 288px; }
  .panel--support .content { position: absolute; left: 20px; top: 68px; width: 296px; }
  .service-title {
    font-family: "Vollkorn", Georgia, serif;
    font-weight: 600; font-size: 16.5px; line-height: 1.2;
    color: var(--brand-blue); margin-bottom: 2px;
  }
  .service-text {
    font-size: 13.3px; line-height: 1.42; text-align: justify;
  }
  .care-emblem { position: absolute; left: 700px; top: 410px; }
</style>
</head>
<body>
  <main class="brochure">
    <svg class="decor" viewBox="0 0 1020 770" aria-hidden="true">
      <!-- bottom band -->
      <path d="M0 728 C 300 745, 700 742, 1020 700 L1020 770 L0 770 Z" fill="var(--soft-blue)"/>
      <!-- intro swoosh -->
      <path d="M0 392 C 110 430, 230 420, 340 372" fill="none" stroke="var(--pale-line)" stroke-width="1.2"/>
      <path d="M0 400 C 120 438, 240 428, 340 384" fill="none" stroke="var(--pale-line)" stroke-width="0.8"/>
      <path d="M0 438 C 110 452, 240 445, 340 428 C 240 455, 110 468, 0 460 Z" fill="var(--deep-blue)"/>
      <!-- support panel swoosh -->
      <path d="M680 735 C 800 720, 930 690, 1020 640 L1020 660 C 930 705, 800 732, 680 742 Z" fill="var(--deep-blue)"/>
      <path d="M680 742 C 800 732, 930 705, 1020 660 L1020 770 L680 770 Z" fill="var(--soft-blue)"/>
    </svg>

    <section class="panel panel--intro">
      <h1 class="intro-heading">Experts in Customized health care By compounding medications, we can improve patient outcomes and simplify medication administration caregivers</h1>
      <ul class="feature-list">
        <li>Customized Combinations simplify medication admistration</li>
        <li>Dosage form Changes</li>
        <li>Transdermal Pain Management for site specific therapy</li>
        <li>Sugar-Free therapy for diabetic patients</li>
        <li>Lactose Capsules</li>
        <li>Customized dosage for kidney or liver failure patients</li>
      </ul>
    </section>

    <section class="panel panel--services">
      <div class="content">
        <article class="service-block">
          <h2 class="service-title">Service:</h2>
          <p class="service-text">Our service sets us apart from retail pharmacies as well as large impersonal pharmacies. As your pharmacy partner, you'll have access to our pharmacy owners knowledge staff to address concerns, find solutions, and ultimately provide better care while increasing your profitability.</p>
        </article>
        <article class="service-block">
          <h2 class="service-title">Timely Deliveries</h2>
          <p class="service-text">When it comes to timely deliveries, Harborview has multiple solutions to get you the medications you need quickly. With our pharmacy network, we can deliver medications at anytime, for any reason.</p>
        </article>
        <article class="service-block">
          <h2 class="service-title">MAR or EMAR</h2>
          <p class="service-text">We support EMAR or provide paper MARs if desired. Our goal is to work with your current system, not against it.</p>
        </article>
        <article class="service-block">
          <h2 class="service-title">Customized Formularies</h2>
          <p class="service-text">We help you manage healthcare costs and limit staff dispensing time by creating formularies that focus on generic and customized compounded medications.</p>
        </article>
        <article class="service-block">
          <h2 class="service-title">Technology Solutions</h2>
          <p class="service-text">Harborview provides great time saving technology solutions that you won't find with other local retail pharmacies. We are constantly offer new and exciting ways to reduce staff time and increase profitability</p>
        </article>
        <article class="service-block">
          <h2 class="service-title">Medicare Part D Partners</h2>
          <p class="service-text">We handle therapeutic interchange, prior authorizations, and physician global authorizations so you don't have to.</p>
        </article>
      </div>
    </section>

    <section class="panel panel--support">
      <div class="content">
        <article class="service-block">
          <h2 class="service-title">Medicare Part A</h2>
          <p class="service-text">Utilizing our pharmacy network, we minimize billing issues with price transparency and accuracy. This allows us focus on corporate strategies to manage your pharmacy expenses. Monthly reports helps identify trends, non-formulary utilization and clinical standards to ensure your facility is saving time and money.</p>
        </article>
        <article class="service-block">
          <h2 class="service-title">Consultant Pharmacists</h2>
          <p class="service-text">Our pharmacists provide regulatory compliance assistance to minimize your risk and reduce issues during facility surveys.</p>
        </article>
        <article class="service-block">
          <h2 class="service-title">Continuing Education</h2>
          <p class="service-text">CE for caretakers leads to better outcomes for your residents and your bottom line.</p>
        </article>
      </div>
    </section>

    <svg class="care-emblem" width="260" height="290" viewBox="0 0 260 290" role="img" aria-label="Cross-shaped illustration made of small blue medical icons">
      <defs>
        <linearGradient id="emblemTone" x1="0" y1="0" x2="1" y2="1">
          <stop offset="0" stop-color="#5aa9d6"/>
          <stop offset="1" stop-color="#2c86c0"/>
        </linearGradient>
      </defs>
      <path d="M85 0 H175 V95 H260 V190 H175 V290 H85 V190 H0 V95 H85 Z" fill="url(#emblemTone)" opacity="0.8"/>
    </svg>
  </main>
</body>
</html>
```